Therapy Dog Organization Website

Looking for a website that is user friendly, welcoming, dog themed and has the following pages and links:
*Click here to join - links to a jot form
*Click here to donate - links to our paypal page
*Request a visit - links to a jot form
*Facebook Follow Link
*Instagram Follow Link
*Our team - images uploaded to showcase our dogs
*Donors and Referrals Page - Where I can update as donations and referrals come in.
*Online store. Currently this is in Jot Form but I would like a store front. I would not want this to be a link but rather a hidden page, something like www.hollowbirch.org/teamstore.

Please visit www.hollowbirch.org to see what we have right now designed simply in Canva. Dog photos can be provided to use in images.

Note: I have funds from a grant that I have to spend to add gratuity to the project winner.

```html
<!DOCTYPE html>
<html lang="en">
<head>
<meta charset="utf-8">
<title>Hollow Birch Therapy Dogs</title>
<link rel="stylesheet" href="https://fonts.googleapis.com/css2?family=Fredoka:wght@600;700&family=Nunito:wght@400;600;700&display=swap">
<style>
:root{
  --orange:#E67E22;
  --orange-dark:#D35400;
  --cream:#FBF2E0;
  --navy:#2C3E50;
  --text:#7A7F87;
  --green:#2ECC71;
  --green-dark:#27AE60;
  --white:#FFFFFF;
}
*{box-sizing:border-box;margin:0;padding:0}
html,body{width:1200px;height:3710px;overflow:hidden}
body{font-family:'Nunito',sans-serif;color:var(--text);background:var(--white);position:relative}
.display{font-family:'Fredoka',sans-serif;font-weight:700;color:var(--navy)}
.abs{position:absolute}
svg{display:block}

.site-header{position:absolute;left:0;top:0;width:1200px;height:94px;background:var(--white);box-shadow:0 2px 10px rgba(0,0,0,.06);z-index:2}
.brand{position:absolute;left:84px;top:26px;display:flex;align-items:center;gap:10px}
.brand-dot{width:36px;height:36px;border-radius:50%;background:var(--orange)}
.brand-name{font-family:'Nunito',sans-serif;font-weight:700;font-size:27px;color:var(--orange)}
.badge{position:absolute;left:339px;top:17px;width:50px;height:58px;border-radius:50%/45%;background:#D4A72C}
.nav{position:absolute;top:29px;left:485px;display:flex;align-items:center;font-size:14px;font-weight:600;color:var(--navy)}
.nav a{text-decoration:none;color:inherit}
.nav .active{background:var(--orange);color:var(--white);border-radius:6px;width:68px;height:34px;display:flex;align-items:center;justify-content:center}
.social-round{position:absolute;width:36px;height:36px;border-radius:50%;background:#FCEBD6}

.photo{position:absolute;border-radius:14px;box-shadow:0 10px 30px rgba(0,0,0,.15)}

.hero{position:absolute;left:0;top:94px;width:1200px;height:533px;background:var(--cream)}
.hero h1{position:absolute;left:17px;top:112px;font-size:46px;line-height:54px}
.hero .tagline{position:absolute;left:17px;top:238px;font-family:'Fredoka',sans-serif;font-weight:700;font-size:22px;color:var(--orange)}
.hero p{position:absolute;left:17px;top:287px;width:660px;font-size:16px;line-height:29px}
.btn{position:absolute;display:flex;align-items:center;justify-content:center;gap:8px;border-radius:6px;font-weight:700;font-size:14px;text-decoration:none}
.btn-orange{background:var(--orange);color:var(--white)}
.btn-green{background:var(--green);color:var(--white)}
.btn-white{background:var(--white);color:var(--orange)}

.visit-card{position:absolute;left:84px;top:699px;width:1032px;height:397px;border-radius:16px;background:linear-gradient(135deg,#E67E22,#D35400);box-shadow:0 14px 30px rgba(211,84,0,.25);text-align:center;color:var(--white)}
.visit-card h2{position:absolute;top:158px;width:100%;font-family:'Fredoka',sans-serif;font-weight:700;font-size:37px;color:var(--white)}
.visit-card p{position:absolute;top:218px;width:100%;font-size:15.5px;line-height:27px}

.band{position:absolute;left:0;width:1200px}
.cream{background:var(--cream)}
.sec-title{position:absolute;font-size:38px}
.sec-text{position:absolute;font-size:15px;line-height:28px}
.stat{position:absolute;width:170px;text-align:center}
.stat-num{font-family:'Fredoka',sans-serif;font-weight:700;font-size:36px;color:var(--orange)}
.stat-label{font-size:13px;margin-top:6px}

.cta{position:absolute;left:0;top:3080px;width:1200px;height:298px;background:linear-gradient(135deg,var(--green),var(--green-dark));text-align:center;color:var(--white)}
.cta h2{position:absolute;top:72px;width:100%;font-family:'Fredoka',sans-serif;font-weight:700;font-size:38px;color:var(--white)}
.cta p{position:absolute;top:130px;width:100%;font-size:16px}

.site-footer{position:absolute;left:0;top:3378px;width:1200px;height:332px;background:var(--navy);color:#C9D1DA;font-size:14px}
.footer-col{position:absolute;top:56px}
.footer-col h4{font-family:'Fredoka',sans-serif;font-weight:700;font-size:17px;color:var(--white)}
.footer-col h4::after{content:"";display:block;width:36px;height:3px;background:var(--orange);margin-top:6px}
.footer-col ul{list-style:none;margin-top:10px}
.footer-col li{height:34px;line-height:20px;display:flex;gap:12px;align-items:flex-start}
.footer-social{position:absolute;width:40px;height:40px;border-radius:50%;background:rgba(255,255,255,.12)}
.footer-rule{position:absolute;left:84px;top:277px;width:1032px;height:1px;background:rgba(255,255,255,.12)}
.copyright{position:absolute;top:297px;width:100%;text-align:center;font-size:12.5px;color:#9AA5B1}
</style>
</head>
<body>

<header class="site-header">
  <div class="brand"><span class="brand-dot"></span><span class="brand-name">Hollow Birch</span></div>
  <span class="badge" aria-label="Evaluator certification badge"></span>
  <nav class="nav">
    <a class="active" href="#">Home</a>
    <a href="#" style="margin-left:41px">Our Team</a>
    <a href="#" style="margin-left:55px">Donors &amp; Referrals</a>
    <a href="#" style="margin-left:55px">Store</a>
  </nav>
  <a class="social-round" style="left:1034px;top:27px" aria-label="Social profile one"></a>
  <a class="social-round" style="left:1080px;top:27px" aria-label="Social profile two"></a>
</header>

<section class="hero">
  <h1 class="display">Bringing Comfort, Joy &amp;<br>Unconditional Love</h1>
  <div class="tagline">One Paw at a Time</div>
  <p>Our therapy dogs bring warmth and healing to those who need it most. Join our pack and make a difference in your community.</p>
  <a class="btn btn-orange" style="left:17px;top:373px;width:188px;height:46px" href="#">
    <svg width="15" height="14" viewBox="0 0 24 22"><path fill="#fff" d="M12 22 2 12A6 6 0 0 1 12 4a6 6 0 0 1 10 8z"/></svg>Click Here to Join</a>
  <a class="btn btn-green" style="left:219px;top:373px;width:210px;height:46px" href="#">
    <svg width="16" height="14" viewBox="0 0 24 22"><circle cx="13" cy="6" r="4" fill="#fff"/><path fill="#fff" d="M2 14h6l4 3h8v3H2z"/></svg>Click Here to Donate</a>
  <div class="photo" style="left:712px;top:77px;width:469px;height:378px;background:linear-gradient(135deg,#5A4A4C,#2F6E9A 55%,#7B7F8A)" role="img" aria-label="Therapy dogs in blue vests resting with visitors on a carpet"></div>
</section>

<div class="visit-card">
  <svg class="abs" style="left:487px;top:68px" width="58" height="52" viewBox="0 0 58 52" fill="#fff">
    <ellipse cx="10" cy="20" rx="7" ry="9"/><ellipse cx="22" cy="8" rx="7" ry="9"/><ellipse cx="36" cy="8" rx="7" ry="9"/><ellipse cx="48" cy="20" rx="7" ry="9"/>
    <path d="M29 24c-10 0-18 14-18 21 0 6 8 6 18 2 10 4 18 4 18-2 0-7-8-21-18-21z"/>
  </svg>
  <h2>Request a Visit</h2>
  <p>Want our therapy dogs to bring comfort to your facility, school, or event?<br>Fill out our simple request form and we'll schedule a visit.</p>
  <a class="btn btn-white" style="left:430px;top:296px;width:172px;height:46px" href="#">
    <svg width="14" height="14" viewBox="0 0 14 14"><rect x="1" y="2" width="12" height="11" rx="2" fill="#E67E22"/><rect x="3" y="6" width="8" height="1.5" fill="#fff"/><rect x="3" y="0" width="2" height="4" fill="#E67E22"/><rect x="9" y="0" width="2" height="4" fill="#E67E22"/></svg>Request a Visit</a>
</div>

<section class="band cream" style="top:1167px;height:536px">
  <div class="photo" style="left:84px;top:72px;width:489px;height:392px;background:linear-gradient(135deg,#D8D3CC,#6E6A6A 55%,#3A3A3E)" role="img" aria-label="Three fluffy therapy dogs sitting in an office wearing bandanas"></div>
  <h2 class="sec-title display" style="left:627px;top:126px">What We Do</h2>
  <p class="sec-text" style="left:627px;top:189px;width:480px">A Michigan Nonprofit dedicated to bringing comfort, joy, and unconditional love to those who need it most. Our certified therapy dogs visit hospitals, nursing homes, schools, and disaster areas to provide emotional support and companionship.</p>
  <div class="stat" style="left:614px;top:332px"><div class="stat-num">50+</div><div class="stat-label">Therapy Dogs</div></div>
  <div class="stat" style="left:785px;top:332px"><div class="stat-num">1000+</div><div class="stat-label">Visits Made</div></div>
  <div class="stat" style="left:957px;top:332px"><div class="stat-num">500+</div><div class="stat-label">Lives Touched</div></div>
</section>

<section class="band" style="top:1703px;height:537px">
  <h2 class="sec-title display" style="left:84px;top:72px">Our Story</h2>
  <p class="sec-text" style="left:84px;top:130px;width:470px">Every wag tells a story - and ours began with a simple belief: the love of a dog can change lives.</p>
  <p class="sec-text" style="left:84px;top:212px;width:490px">What started with a few volunteers and their dogs has grown into a community dedicated to bringing comfort and joy wherever it's needed most. From hospitals to schools and senior centers, our therapy dog teams share moments of connection, calm, and healing - one visit at a time.</p>
  <p class="sec-text" style="left:84px;top:380px;width:470px">At the heart of our mission is a simple truth - sometimes the best kind of therapy comes with four paws and a wagging tail.</p>
  <div class="photo" style="left:627px;top:72px;width:489px;height:393px;background:linear-gradient(135deg,#3B4A63,#D9A86A 50%,#2F6E9A)" role="img" aria-label="Smiling golden therapy dog in a blue vest and pink bandana"></div>
</section>

<section class="band cream" style="top:2240px;height:536px">
  <div class="photo" style="left:84px;top:71px;width:489px;height:393px;background:linear-gradient(135deg,#6C5A55,#3E3E44 50%,#2F7FB0)" role="img" aria-label="Merle therapy dog close up in a blue vest and floral bandana"></div>
  <h2 class="sec-title display" style="left:627px;top:140px">Our Mission</h2>
  <p class="sec-text" style="left:627px;top:202px;width:480px">To certify, and deploy therapy dog teams that promote emotional<br>well-being, reduce stress, and foster empathy. We are dedicated to improving quality of life by bringing the unconditional love and calming presence of therapy dogs to those in need, while upholding the highest standards of animal welfare, professionalism, and community service.</p>
</section>

<section class="band" style="top:2776px;height:304px;text-align:center">
  <h2 class="display" style="position:absolute;top:70px;width:100%;font-size:38px">Our Purpose</h2>
  <p class="sec-text" style="left:92px;top:126px;width:1016px;font-size:15.5px;line-height:26px">Our purpose is to share the comfort, joy, and healing power of the human animal bond. We connect trained therapy dog teams with people in need of emotional support, companionship, and encouragement in hospitals, schools, senior communities, and beyond. Through every visit, we aim to lift spirits, ease stress, and remind people that kindness and connection can come on four paws and a wagging tail.</p>
</section>

<section class="cta">
  <h2>Join Our Pack Today</h2>
  <p>Whether you want to volunteer, donate, or schedule a visit, we'd love to hear from you!</p>
  <a class="btn btn-white" style="left:406px;top:180px;width:199px;height:46px" href="#">
    <svg width="18" height="14" viewBox="0 0 18 14" fill="#E67E22"><circle cx="6" cy="4" r="3.5"/><path d="M0 14c0-4 3-6 6-6s6 2 6 6z"/><rect x="13" y="5" width="5" height="1.6"/><rect x="14.7" y="3.3" width="1.6" height="5"/></svg>Become a Member</a>
  <a class="btn btn-white" style="left:618px;top:180px;width:176px;height:46px" href="#">
    <svg width="14" height="14" viewBox="0 0 14 14"><rect x="1" y="2" width="12" height="11" rx="2" fill="#E67E22"/><rect x="3" y="6" width="8" height="1.5" fill="#fff"/></svg>Request a Visit</a>
</section>

<footer class="site-footer">
  <div class="abs" style="left:84px;top:60px;display:flex;align-items:center;gap:10px"><span class="brand-dot" style="background:#fff"></span><span class="brand-name" style="color:#fff">Hollow Birch</span></div>
  <p class="abs" style="left:84px;top:146px;width:330px;font-size:13.5px;line-height:24px">Bringing comfort, joy and unconditional love - One Paw at a Time.</p>
  <a class="footer-social" style="left:84px;top:199px" aria-label="Social profile one"></a>
  <a class="footer-social" style="left:134px;top:199px" aria-label="Social profile two"></a>

  <div class="footer-col" style="left:457px"><h4>Quick Links</h4><ul><li>Home</li><li>Our Team</li><li>Donors &amp; Referrals</li><li>Team Store</li></ul></div>
  <div class="footer-col" style="left:660px"><h4>Get Involved</h4><ul><li>Join Our Pack</li><li>Request a Visit</li><li>Donate</li></ul></div>
  <div class="footer-col" style="left:863px"><h4>Contact Us</h4><ul>
    <li><svg width="15" height="12" viewBox="0 0 15 12" style="margin-top:4px"><rect width="15" height="12" rx="1.5" fill="#E67E22"/><path d="M1 1l6.5 5L14 1" stroke="#2C3E50" stroke-width="1.4" fill="none"/></svg>info@hollowbirch.org</li>
    <li><svg width="15" height="15" viewBox="0 0 24 24" style="margin-top:3px"><path fill="#E67E22" d="M6.6 10.8a15 15 0 0 0 6.6 6.6l2.2-2.2c.3-.3.7-.4 1-.2 1.1.4 2.3.6 3.6.6.6 0 1 .4 1 1V20c0 .6-.4 1-1 1A17 17 0 0 1 3 4c0-.6.4-1 1-1h3.5c.6 0 1 .4 1 1 0 1.3.2 2.5.6 3.6.1.3 0 .7-.2 1z"/></svg>(555) 201-3948</li>
  </ul></div>

  <div class="footer-rule"></div>
  <p class="copyright">© 2026 Hollow Birch Therapy Dogs. All rights reserved.</p>
</footer>

</body>
</html>
```